Tobin Quartz Portal Page . It's guarantee project!

We need a clean and professional modern web application portal page
That includes the Login & Application Selection screen

Also, I need to design both Desktop and Mobile sizes.
We have an example design for our target

The application is Jetty Schedule and related data.
Our client is a bit conservative.

Theme color preferred : #00508B (main) #DF0D83 (secondary)

Target Market(s)

Oil & Fuel & Gasoline

Number of Pages Required

2 page

Font styles to use
Sans Serif

Colors
0054AA
0677BA
7BADD7
CADEEF
E8F1F8
E54698
E96AAD
F1A4CE
F9D9EA
FCEFF6

Requirements
Must have
• Login Page & Main Screen

```html
<!DOCTYPE html>
<html lang="en">
<head>
<meta charset="UTF-8">
<title>Tobin Quartz — Select an Application</title>
<link href="https://fonts.googleapis.com/css2?family=Bebas+Neue&family=Roboto:wght@400;500&display=swap" rel="stylesheet">
<style>
  :root {
    --brand-blue: #0054AA;
    --header-blue: #0057AB;
    --text-muted: #777777;
    --card-bg: #FFFFFF;
    --page-bg: #FFFFFF;
    --illus-pink: #F1A4CE;
    --illus-pale: #FCEFF6;
    --illus-blue: #CADEEF;
    --illus-soft: #E8F1F8;
  }
  * { box-sizing: border-box; margin: 0; padding: 0; }
  html, body {
    width: 1200px;
    height: 3243px;
    overflow: hidden;
    background: var(--page-bg);
    font-family: "Roboto", Arial, sans-serif;
  }
  .top-bar {
    height: 223px;
    background: var(--header-blue);
    display: flex;
    align-items: center;
    justify-content: space-between;
    padding: 0 70px 0 122px;
    color: #fff;
  }
  .home-link {
    display: flex;
    align-items: center;
    gap: 34px;
    font-family: "Bebas Neue", Impact, sans-serif;
    font-size: 52px;
    letter-spacing: 1px;
    color: #fff;
    text-decoration: none;
  }
  .home-link svg { width: 50px; height: 50px; }
  .user-box { display: flex; align-items: center; gap: 58px; }
  .user-info { text-align: right; }
  .user-name {
    font-family: "Bebas Neue", Impact, sans-serif;
    font-size: 38px;
    letter-spacing: 1px;
    line-height: 1.1;
  }
  .user-email { font-size: 30px; opacity: 0.9; margin-top: 6px; }
  .user-avatar {
    width: 112px; height: 112px; border-radius: 50%;
    background: linear-gradient(180deg, #E9C9A0 0%, #C9B7A0 55%, #5C6E7C 100%);
  }
  .intro { text-align: center; margin-top: 197px; }
  .intro h1 {
    font-family: "Bebas Neue", Impact, sans-serif;
    font-weight: 400;
    font-size: 118px;
    letter-spacing: 2px;
    color: var(--brand-blue);
    line-height: 1;
  }
  .intro p {
    font-size: 42px;
    line-height: 70px;
    color: var(--text-muted);
    margin: 22px auto 0;
    width: 900px;
  }
  .app-list {
    margin: 92px auto 0;
    width: 976px;
    display: flex;
    flex-direction: column;
    gap: 56px;
  }
  .app-card {
    background: var(--card-bg);
    border-radius: 39px;
    box-shadow: 0 20px 70px rgba(0, 0, 0, 0.12);
    display: flex;
    flex-direction: column;
    align-items: center;
    padding: 45px 60px 0;
    height: 745px;
  }
  .app-card.short { height: 681px; }
  .app-illustration {
    width: 370px; height: 377px;
    border-radius: 50%;
    background: radial-gradient(circle at 50% 50%, var(--illus-pink) 0%, var(--illus-pale) 55%, var(--illus-soft) 75%, #fff 100%);
  }
  .app-title {
    font-family: "Bebas Neue", Impact, sans-serif;
    font-weight: 400;
    font-size: 54px;
    letter-spacing: 1.5px;
    color: var(--brand-blue);
    margin-top: 68px;
    line-height: 1;
  }
  .app-desc {
    font-size: 40px;
    line-height: 64px;
    color: var(--text-muted);
    text-align: center;
    margin-top: 24px;
  }
</style>
</head>
<body>
  <header class="top-bar">
    <a class="home-link" href="#">
      <svg viewBox="0 0 24 24" fill="none" stroke="#fff" stroke-width="2.2" stroke-linejoin="round">
        <path d="M3 10.5 12 3l9 7.5V21h-6v-6h-6v6H3z"/>
      </svg>
      Home
    </a>
    <div class="user-box">
      <div class="user-info">
        <div class="user-name">Mara Lind</div>
        <div class="user-email">mara.lind@harborline.test</div>
      </div>
      <div class="user-avatar" role="img" aria-label="User profile photo"></div>
    </div>
  </header>

  <section class="intro">
    <h1>Select an Application</h1>
    <p>Choose from the available options to manage your shipping needs.</p>
  </section>

  <main class="app-list">
    <article class="app-card">
      <div class="app-illustration" role="img" aria-label="Illustration of a calendar with a rising trend arrow and gears"></div>
      <h2 class="app-title">Jetty Planning</h2>
      <p class="app-desc">Tools and schedules to plan your jetty operations.</p>
    </article>
    <article class="app-card">
      <div class="app-illustration" role="img" aria-label="Illustration of a ship, trucks and map pins along a delivery route"></div>
      <h2 class="app-title">Jetty Tracking</h2>
      <p class="app-desc">Real-time tracking of jetty operations and shipments.</p>
    </article>
    <article class="app-card short">
      <div class="app-illustration" role="img" aria-label="Illustration of an analyst beside rising bars and a coin"></div>
      <h2 class="app-title">Jetty/Port Performance</h2>
      <p class="app-desc">Monitor and optimize port performance metrics.</p>
    </article>
  </main>
</body>
</html>
```